Corvane Tables business cards

I’d like a business card design that includes my logo, a tag line and my contact info. Black, textured background. My contact info color should match the orange and blue gradients. Tagline under logo: “Wooden Tables and Furniture of the Highest Quality”

Target Market(s)

High end furniture buyers

Contact Information for Business Card

Contact info, logo and tagline

```html
<!DOCTYPE html>
<html lang="en">
<head>
<meta charset="utf-8">
<title>Corvane Tables business cards</title>
<link href="https://fonts.googleapis.com/css2?family=Arimo:wght@400;700&family=Tinos:wght@700&display=swap" rel="stylesheet">
<style>
  :root {
    --backdrop: #2b2b2e;
    --card: #0f1013;
    --card-edge: #1a1b1f;
    --orange: #ef7a3b;
    --orange-deep: #e4582a;
    --blue: #3d8fd9;
    --white: #f4f4f4;
  }
  html, body {
    margin: 0;
    padding: 0;
    width: 1200px;
    height: 779px;
    overflow: hidden;
    background: var(--backdrop);
  }
  .canvas {
    position: relative;
    width: 1200px;
    height: 779px;
  }
  .card {
    position: absolute;
    background: radial-gradient(circle at 40% 30%, var(--card-edge), var(--card) 70%);
    box-shadow: 0 10px 30px rgba(0,0,0,.45);
    font-family: "Arimo", Arial, sans-serif;
    color: var(--white);
  }
  /* Back card, portrait */
  .card-back {
    left: 102px;
    top: 92px;
    width: 340px;
    height: 595px;
  }
  .back-content {
    position: absolute;
    left: 44px;
    top: 56px;
    right: 30px;
  }
  .brand {
    display: flex;
    align-items: center;
    gap: 10px;
  }
  .brand-dot {
    border-radius: 50%;
    background: var(--orange);
    flex: none;
  }
  .brand-name {
    font-family: "Arimo", Arial, sans-serif;
    font-weight: 400;
    color: var(--orange);
    white-space: nowrap;
  }
  .card-back .brand-dot { width: 14px; height: 14px; }
  .card-back .brand-name { font-size: 26px; }
  .person { margin-top: 44px; }
  .person-name {
    font-family: "Tinos", "Times New Roman", serif;
    font-weight: 700;
    font-size: 21px;
    color: var(--orange);
    margin: 0;
  }
  .person-title {
    font-size: 15px;
    color: var(--blue);
    margin: 4px 0 0;
  }
  .address {
    margin-top: 34px;
    font-size: 15px;
    line-height: 1.35;
  }
  .contacts {
    margin-top: 30px;
    font-size: 15px;
    line-height: 1.4;
    list-style: none;
    padding: 0;
  }
  .contacts .label {
    color: var(--orange);
    font-weight: 700;
    margin-right: 4px;
  }
  /* Front card, landscape */
  .card-front {
    left: 502px;
    top: 219px;
    width: 595px;
    height: 340px;
  }
  .front-brand {
    position: absolute;
    left: 0;
    right: 0;
    top: 96px;
    justify-content: center;
  }
  .card-front .brand-dot { width: 22px; height: 22px; }
  .card-front .brand-name { font-size: 46px; }
  .tagline {
    position: absolute;
    left: 0;
    right: 0;
    top: 212px;
    text-align: center;
    font-weight: 700;
    font-size: 17px;
    letter-spacing: .2px;
    color: var(--white);
  }
</style>
</head>
<body>
<main class="canvas">
  <section class="card card-back" aria-label="Card back">
    <div class="back-content">
      <div class="brand">
        <span class="brand-dot"></span>
        <span class="brand-name">Corvane Tables</span>
      </div>
      <div class="person">
        <p class="person-name">Daniel Mercer</p>
        <p class="person-title">President</p>
      </div>
      <div class="address">
        4127 Ashcombe Lane<br>
        Maple Hollow, NY 11290
      </div>
      <ul class="contacts">
        <li><span class="label">P :</span>(555) 2184-6630</li>
        <li><span class="label">C :</span>(555) 7391-4072</li>
        <li><span class="label">F :</span>(555) 5026-8114</li>
        <li><span class="label">E :</span>hello@corvanetables.com</li>
        <li><span class="label">W :</span>www.corvanetables.com</li>
      </ul>
    </div>
  </section>

  <section class="card card-front" aria-label="Card front">
    <div class="brand front-brand">
      <span class="brand-dot"></span>
      <span class="brand-name">Corvane Tables</span>
    </div>
    <p class="tagline">Wooden Tables and Furniture of the Highest Quality</p>
  </section>
</main>
</body>
</html>
```